Bottle label design for a mulberry brandy

Please create a label design for a mulberry brandy. The registered brand name is "Kolvat"
The brandy will be produced in Armenia from 100% mulberry.
Color of the product: transparent.
The product will be sold worldwide. The price will be between 30 and 50 USD. So the product will be in premium category.
Therefore we need a solid design, appropriate to the product price category. The design, however, needs to be modern and optimistic.
You can have mulberries on the label or not have, it is up to you.
We have chosen for the product some bottle types, the links to the available bottles you can find in the attachment. Ideally you show a picture of your label on the bottle you selected.

Target Market(s)

worldwide

```html
<!DOCTYPE html>
<html lang="en">
<head>
<meta charset="utf-8">
<title>Kolvat Mulberry Brandy – Label</title>
<link rel="stylesheet" href="https://fonts.googleapis.com/css2?family=Libre+Baskerville:wght@400;700&display=swap">
<style>
  :root {
    --maroon: #7a2421;
    --maroon-deep: #661c1a;
    --cream: #f7f1d3;
    --cream-warm: #f1e4b8;
    --gold: #d99a55;
    --gold-light: #f0cf95;
    --copper: #c9753a;
    --brown-text: #8a3a1f;
    --stripe-a: #e9d7b0;
    --stripe-b: #c9ad86;
    --ink-light: #f3e6c9;
  }
  * { margin: 0; padding: 0; box-sizing: border-box; }
  html, body {
    width: 1190px;
    height: 1200px;
    overflow: hidden;
    background: #ffffff;
    font-family: "Libre Baskerville", Georgia, serif;
  }
  .canvas { position: relative; width: 1190px; height: 1200px; }

  .label {
    position: absolute;
    left: 174px; top: 106px;
    width: 842px; height: 987px;
    background: var(--maroon);
  }
  .label__frame {
    position: absolute;
    inset: 14px;
    border: 2px solid var(--gold);
    pointer-events: none;
  }

  .panel {
    position: absolute;
    left: 39px; top: 39px;
    width: 764px; height: 577px;
    background: var(--cream);
    overflow: hidden;
  }
  .panel__crown {
    position: absolute;
    left: 0; top: 0; width: 100%; height: 117px;
    background: linear-gradient(90deg, var(--copper) 0%, var(--gold-light) 30%, var(--cream) 50%, var(--gold-light) 70%, var(--copper) 100%);
  }
  .panel__sun {
    position: absolute;
    left: 332px; top: 14px; width: 100px; height: 88px;
    border-radius: 50% 50% 40% 40%;
    background: radial-gradient(circle, var(--gold) 0%, rgba(217,154,85,0.35) 55%, rgba(217,154,85,0) 72%);
  }
  .panel__flourish {
    position: absolute;
    top: 28px; width: 150px; height: 34px;
    border-radius: 50%;
    background: linear-gradient(90deg, rgba(255,255,255,0.6), rgba(201,117,58,0.35));
  }
  .panel__flourish--left { left: 20px; }
  .panel__flourish--right { right: 20px; transform: scaleX(-1); }

  .panel__stripes {
    position: absolute;
    top: 117px; width: 129px; height: 443px;
    background: linear-gradient(180deg, var(--stripe-a), var(--stripe-b));
  }
  .panel__stripes--left { left: 8px; }
  .panel__stripes--right { right: 8px; }

  .brand {
    position: absolute;
    left: 0; right: 0; top: 248px;
    text-align: center;
    font-weight: 700;
    font-size: 46px;
    letter-spacing: 6px;
    color: var(--maroon);
  }
  .strength {
    position: absolute;
    left: 0; right: 0; top: 312px;
    text-align: center;
    font-weight: 700;
    font-size: 66px;
    color: var(--copper);
  }
  .fruit {
    position: absolute;
    left: 0; right: 0; top: 400px;
    text-align: center;
    font-weight: 700;
    font-size: 40px;
    letter-spacing: 3px;
    color: var(--brown-text);
  }
  .fruit__swoosh { position: absolute; left: 322px; top: 460px; }

  .panel__band {
    position: absolute;
    left: 0; top: 548px; width: 100%; height: 22px;
    background: linear-gradient(90deg, var(--copper), var(--gold-light), var(--copper));
    border-top: 2px solid var(--gold);
  }

  .origin {
    position: absolute;
    left: 39px; top: 640px;
    width: 764px; height: 84px;
    background: var(--cream);
    border-top: 3px solid var(--gold);
    border-bottom: 3px solid var(--gold);
    display: flex; align-items: center; justify-content: center;
    font-size: 22px;
    letter-spacing: 2px;
    color: var(--brown-text);
  }

  .spec {
    position: absolute;
    top: 765px;
    font-size: 17px;
    color: var(--ink-light);
  }
  .spec--abv { left: 66px; }
  .spec--volume { right: 66px; }

  .seal { position: absolute; left: 301px; top: 728px; }

  .footer-flourish {
    position: absolute;
    top: 858px; width: 170px; height: 30px;
    border-radius: 50%;
    background: linear-gradient(90deg, rgba(217,154,85,0.2), var(--gold));
  }
  .footer-flourish--left { left: 64px; }
  .footer-flourish--right { right: 64px; transform: scaleX(-1); }
  .footer-rule {
    position: absolute;
    left: 250px; right: 250px; top: 872px;
    height: 2px; background: var(--gold);
  }
  .footer-code {
    position: absolute;
    left: 0; right: 0; top: 925px;
    text-align: center;
    font-size: 15px;
    letter-spacing: 2px;
    color: var(--ink-light);
  }
</style>
</head>
<body>
<main class="canvas">
  <section class="label">
    <div class="label__frame"></div>

    <div class="panel">
      <div class="panel__crown"></div>
      <div class="panel__flourish panel__flourish--left" role="img" aria-label="Decorative scroll flourish"></div>
      <div class="panel__sun" role="img" aria-label="Stylised sun emblem"></div>
      <div class="panel__flourish panel__flourish--right" role="img" aria-label="Decorative scroll flourish"></div>

      <div class="panel__stripes panel__stripes--left" role="img" aria-label="Engraved line pattern"></div>
      <div class="panel__stripes panel__stripes--right" role="img" aria-label="Engraved line pattern"></div>

      <div class="brand">KOLVAT</div>
      <div class="strength">100%</div>
      <div class="fruit">MULBERRY</div>
      <svg class="fruit__swoosh" width="120" height="14" viewBox="0 0 120 14">
        <path d="M4 8 Q60 0 116 8" stroke="#c9753a" stroke-width="3" fill="none" stroke-linecap="round"/>
      </svg>

      <div class="panel__band"></div>
    </div>

    <div class="origin">PRODUCED IN ARMENIA</div>

    <span class="spec spec--abv">40% VOL</span>
    <span class="spec spec--volume">500 ML</span>

    <svg class="seal" width="240" height="130" viewBox="0 0 240 130">
      <polygon points="120,6 129,32 157,32 134,48 143,74 120,58 97,74 106,48 83,32 111,32"
               fill="#d99a55" stroke="#f0cf95" stroke-width="2"/>
      <path id="seal-arc" d="M20 72 Q120 152 220 72" fill="none"/>
      <text font-family="Libre Baskerville, serif" font-size="15" fill="#f3e6c9" letter-spacing="2">
        <textPath href="#seal-arc" startOffset="50%" text-anchor="middle">MULBERRY BRANDY</textPath>
      </text>
    </svg>

    <div class="footer-flourish footer-flourish--left" role="img" aria-label="Decorative scroll flourish"></div>
    <div class="footer-rule"></div>
    <div class="footer-flourish footer-flourish--right" role="img" aria-label="Decorative scroll flourish"></div>

    <div class="footer-code">DISTILLED TWICE</div>
  </section>
</main>
</body>
</html>
```